Current Employment Opportunities Email Template

We would like to redesign our internal job listing email template we send out each month. The email service we use is MailChimp and would like the template to be easy to edit when updating job postings. I attached an example below.

Font styles to use
Sans Serif

Colors

Designer to choose colors to be used in the design.

```html
<!DOCTYPE html>
<html lang="en">
<head>
<meta charset="utf-8">
<title>Talent Opportunities Email</title>
<link href="https://fonts.googleapis.com/css2?family=Roboto+Condensed:wght@700&family=Open+Sans:wght@400;600;700&display=swap" rel="stylesheet">
<style>
:root{
  --teal:#44736f;
  --teal-tint:#ebf1f0;
  --accent:#d93a0b;
  --page:#f7f7f7;
  --white:#ffffff;
  --ink:#2b2b2b;
  --rule:#dcdcdc;
  --card-border:#dfe4e3;
}
*{margin:0;padding:0;box-sizing:border-box}
html,body{width:784px;height:1200px;overflow:hidden}
body{background:var(--page);font-family:'Open Sans',sans-serif;color:var(--ink);position:relative}
.email{position:absolute;left:132px;top:6px;width:520px;height:1194px;background:var(--white)}
.hero{position:relative;height:124px;background:var(--teal);color:var(--white);text-align:center}
.hero__title{font-family:'Roboto Condensed',sans-serif;font-weight:700;font-size:32px;line-height:1;padding-top:26px;letter-spacing:-0.3px}
.hero__rule{position:absolute;left:46px;right:47px;top:69px;height:2px;background:var(--white)}
.hero__sub{position:absolute;left:0;right:0;top:80px;font-size:13.6px}
.hero__pointer{position:absolute;left:246px;top:124px}
.intro{padding:45px 46px 0;text-align:center;font-size:12.2px;line-height:16.8px}
.btn{display:block;background:var(--accent);color:var(--white);font-weight:700;font-size:13px;text-align:center;text-decoration:none;height:36px;line-height:36px;border-radius:1px}
.intro__btn{width:133px;margin:29px auto 0}
.openings{position:absolute;left:0;top:360px;width:520px;height:768px;background:var(--teal-tint)}
.openings__title{font-family:'Roboto Condensed',sans-serif;font-weight:700;font-size:29px;color:var(--teal);text-align:center;margin-top:45px;line-height:1}
.job{position:absolute;left:19px;width:482px;height:202px;background:var(--white);border:1px solid var(--card-border)}
.job__city{position:absolute;left:26px;top:23px;font-family:'Roboto Condensed',sans-serif;font-weight:700;font-size:24.5px;color:var(--teal);line-height:1}
.job__place{position:absolute;right:26px;top:27px;font-size:11px}
.job__rule{position:absolute;left:24px;right:24px;top:58px;height:1px;background:var(--rule)}
.job__role{position:absolute;left:26px;top:70px;font-size:16.4px;line-height:1.3}
.job__area{position:absolute;left:26px;top:98px;font-size:11px;font-weight:600;letter-spacing:.2px}
.job__btn{position:absolute;left:26px;top:132px;width:133px}
.footer__brand{position:absolute;left:0;right:0;top:1158px;text-align:center;font-weight:700;font-size:32px;letter-spacing:1px;color:#1f1f1f;line-height:1}
</style>
</head>
<body>
<main class="email">
  <header class="hero">
    <h1 class="hero__title">Today’s Talent Opportunities</h1>
    <div class="hero__rule"></div>
    <p class="hero__sub">Want to be a part of the most efficient and elite team in the industry?</p>
    <svg class="hero__pointer" width="28" height="14" viewBox="0 0 28 14"><polygon points="0,0 28,0 14,14" fill="#44736f"/></svg>
  </header>
  <section class="intro">
    <p>We’ve got a list of opportunities here at Halden that we’d love for you to strive for! These openings allow you to fully utilize your strengths, walk alongside us as we grow exponentially farther than we could ever dream, and leverage your successes to climb your way up the ladder of professional growth and leadership within our organization!</p>
    <a class="btn intro__btn" href="#">More About Us</a>
  </section>
  <section class="openings">
    <h2 class="openings__title">Current Opportunities</h2>
    <article class="job" style="top:96px">
      <h3 class="job__city">Dallas</h3><span class="job__place">Dallas, TX</span>
      <div class="job__rule"></div>
      <p class="job__role">Lead Restoration Technician</p>
      <p class="job__area">Restoration Technician in the Dallas/Ft. Worth Area</p>
      <a class="btn job__btn" href="#">Learn More</a>
    </article>
    <article class="job" style="top:312px">
      <h3 class="job__city">Dallas</h3><span class="job__place">Dallas, TX</span>
      <div class="job__rule"></div>
      <p class="job__role">Lead Restoration Technician</p>
      <p class="job__area">Restoration Technician in the Dallas/Ft. Worth Area</p>
      <a class="btn job__btn" href="#">Learn More</a>
    </article>
    <article class="job" style="top:528px">
      <h3 class="job__city">Dallas</h3><span class="job__place">Dallas, TX</span>
      <div class="job__rule"></div>
      <p class="job__role">Lead Restoration Technician</p>
      <p class="job__area">Restoration Technician in the Dallas/Ft. Worth Area</p>
      <a class="btn job__btn" href="#">Learn More</a>
    </article>
  </section>
  <footer>
    <div class="footer__brand">HALDEN</div>
  </footer>
</main>
</body>
</html>
```